Recreate a label for a champagne bottle [See attached example]

I'm needing to recreate a label for a champagne bottle label to give as closing gifts to clients when they purchase a home. Please include the following text "Welcome Home", my initials "R.T", "Established Year", the hashtag #BubbLORNE and my logo (attached). I prefer to have a black or white background with a crisp, easy to read cursive font similar to the Dunmore bourbon font. I want it to look as similar of a layout to the Valcorta label as possible

Target Market(s)

Luxury

Font styles to use
Decorative
Script

Colors

Designer to choose only greyscale colors for use in the design.

Requirements
Must have
• "Welcome Home", my initials "R.T", "Established Year", the hashtag #BubbLORNE and my logo
Nice to have
• Clean cursive font, easy to read, luxury look.
Should not have
• Clutter, too much design.

```html
<!DOCTYPE html>
<html lang="en">
<head>
<meta charset="utf-8">
<title>Welcome Home – Champagne Label</title>
<link rel="stylesheet" href="https://fonts.googleapis.com/css2?family=Pinyon+Script&family=Great+Vibes&family=Montserrat:wght@400;500&display=swap">
<style>
  :root {
    --page: #ffffff;
    --label: #231f20;
    --ink: #ffffff;
    --silver: #b9b9b9;
    --silver-dark: #8a8a8a;
    --ornament-fill: #4a4748;
    --ornament-soft: #3a3637;
  }
  * { box-sizing: border-box; margin: 0; padding: 0; }
  html, body {
    width: 1200px; height: 1200px; overflow: hidden;
    background: var(--page);
  }
  .label {
    position: absolute; left: 50px; top: 177px;
    width: 1100px; height: 846px;
    background: var(--label);
    color: var(--ink);
  }
  .frame { position: absolute; inset: 0; width: 100%; height: 100%; }
  .corner-ornament {
    position: absolute; width: 110px; height: 110px;
    background: linear-gradient(135deg, var(--ornament-fill), var(--ornament-soft));
  }
  .corner-ornament.tl { left: 30px; top: 30px; }
  .corner-ornament.tr { right: 30px; top: 30px; }
  .corner-ornament.bl { left: 30px; bottom: 30px; }
  .corner-ornament.br { right: 30px; bottom: 30px; }
  .crest-ornament {
    position: absolute; left: 505px; top: 78px;
    width: 90px; height: 20px; border-radius: 10px;
    background: var(--ornament-fill);
  }
  .initials-ornament {
    position: absolute; top: 408px;
    width: 90px; height: 16px; border-radius: 8px;
    background: var(--ornament-fill);
  }
  .initials-ornament.left { left: 368px; }
  .initials-ornament.right { right: 368px; }
  .headline {
    position: absolute; top: 150px; left: 0; width: 100%;
    text-align: center;
    font-family: "Pinyon Script", cursive;
    font-size: 138px; line-height: 1; font-weight: 400;
    color: var(--ink);
  }
  .initials {
    position: absolute; top: 362px; left: 0; width: 100%;
    text-align: center;
    font-family: "Great Vibes", cursive;
    font-size: 78px; line-height: 1;
    color: var(--ink);
  }
  .established {
    position: absolute; top: 530px; left: 0; width: 100%;
    text-align: center;
    font-family: "Pinyon Script", cursive;
    font-size: 36px; line-height: 1;
    color: var(--ink);
  }
  .hashtag {
    position: absolute; top: 628px; left: 0; width: 100%;
    text-align: center;
    font-family: "Montserrat", sans-serif;
    font-weight: 400; font-size: 36px; letter-spacing: 1.5px;
    color: var(--ink);
  }
  .brand-mark {
    position: absolute; top: 730px; left: 0; width: 100%;
    display: flex; justify-content: center; align-items: center; gap: 12px;
    font-family: "Montserrat", sans-serif;
    font-weight: 500; font-size: 30px; letter-spacing: 3px;
    color: var(--silver);
  }
  .brand-mark .square { width: 16px; height: 16px; background: var(--silver); }
</style>
</head>
<body>
  <main class="label">
    <svg class="frame" viewBox="0 0 1100 846" aria-hidden="true">
      <g fill="none" stroke="var(--silver)" stroke-width="1.5">
        <rect x="20" y="20" width="1060" height="806"/>
        <rect x="28" y="28" width="1044" height="790"/>
      </g>
      <rect x="510" y="8" width="100" height="40" fill="var(--label)"/>
      <polygon points="550,14 562,28 550,42 538,28" fill="var(--silver)"/>
      <circle cx="527" cy="28" r="4" fill="var(--silver)"/>
      <circle cx="573" cy="28" r="4" fill="var(--silver)"/>
      <g stroke="var(--silver)" stroke-width="2" stroke-dasharray="2 5">
        <line x1="400" y1="88" x2="478" y2="88"/>
        <line x1="622" y1="88" x2="700" y2="88"/>
        <line x1="232" y1="596" x2="312" y2="596"/>
        <line x1="826" y1="560" x2="906" y2="560"/>
      </g>
      <path class="ribbon" d="M330 560 Q560 500 835 525 L800 553 L840 578 Q560 555 330 605 L362 582 Z"
            fill="none" stroke="var(--silver)" stroke-width="2.5"/>
    </svg>

    <div class="corner-ornament tl" role="img" aria-label="Filigree corner ornament"></div>
    <div class="corner-ornament tr" role="img" aria-label="Filigree corner ornament"></div>
    <div class="corner-ornament bl" role="img" aria-label="Filigree corner ornament"></div>
    <div class="corner-ornament br" role="img" aria-label="Filigree corner ornament"></div>
    <div class="crest-ornament" role="img" aria-label="Small scroll ornament under the top diamond"></div>
    <div class="initials-ornament left" role="img" aria-label="Swirl flourish left of the initials"></div>
    <div class="initials-ornament right" role="img" aria-label="Swirl flourish right of the initials"></div>

    <h1 class="headline">Welcome Home</h1>
    <p class="initials">R.T</p>
    <p class="established">Established 2023</p>
    <p class="hashtag">#BubbLORNE</p>
    <div class="brand-mark"><span class="square"></span><span>Tarrow Homes</span></div>
  </main>
</body>
</html>
```